SKYWARD LENSWORKS New Wordpress Design Project

Skyward Lensworks is a photo-sharing site for aviation photographers and enthusiasts.

Please redesign the home page (http://www.skywardlensworks.example/) and photo feature page (http://www.skywardlensworks.example/2014/10/borvel-freight-23/).

We like and would like to keep the logo we have, but are open to changing colors on the logo to suit a new color scheme if necessary.
Updates

Hi All, Thank you for taking part in this design competition. Could you please show us your first round design concepts within 24hrs as we hope to show our client them and start providing feedback? Much appreciated, Lex VH BramblePeak Design

Hi All, A few tips: Could you try keep the search bar above the fold Include a section for showing new blog posts Try to integrate an ads a little better also above and below the fold Appreciated, Lex Vh

Target Market(s)

Aviation photographers and enthusiasts of all age groups globally.

Industry/Entity Type

Aviation

Requirements
Must have
• • Clean and consistent layout
• A good way to incorporate advertisements on the home page and photo feature page
• Clear and simple menu navigation
• On home page – call to action to register
• On home page - call to action to upload photos
• On home page – social buttons call to action to follow, circle, like, etc
• On photo feature page – call to action to tweet, +1, Like, etc a photo
Nice to have
• Sites we like

www.quillpane.example
http://www.layoutorchard.example/demo/45176.html
Should not have
• • Unnecessary animations
• No Adobe Flash
• Overly crowded / busy design

```html
<!DOCTYPE html>
<html lang="en">
<head>
<meta charset="utf-8">
<title>Skyward Lensworks</title>
<link rel="stylesheet" href="https://fonts.googleapis.com/css2?family=Arimo:wght@400;700&display=swap">
<style>
:root{
  --ink:#2b2b2b;
  --muted:#8a8a8a;
  --dark-band:#232323;
  --button-dark:#333333;
  --accent:#f39514;
  --white:#ffffff;
  --sky-top:#3f8fd8;
  --sky-mid:#9cc6ec;
  --sky-low:#e8f0f7;
  --ad-blue:#4a5fb0;
  --ad-blue-dark:#2f3f86;
  --sunset-1:#f6b27a;
  --sunset-2:#e8875a;
  --sunset-3:#7e6f86;
  --city-1:#3b3a36;
  --city-2:#1e1d1b;
  --icon-bg:#3a3a3a;
}
*{margin:0;padding:0;box-sizing:border-box}
a{text-decoration:none;color:inherit}
html,body{width:977px;height:1200px;overflow:hidden;background:var(--white)}
body{position:relative;font-family:"Arimo",Arial,sans-serif;color:var(--ink)}
.abs{position:absolute}

/* Hero */
.hero{left:0;top:0;width:977px;height:294px;background:linear-gradient(180deg,var(--sky-top) 0%,var(--sky-mid) 45%,var(--sky-low) 100%)}
.hero-photo{left:0;top:0;width:977px;height:294px;background:radial-gradient(ellipse 360px 70px at 420px 240px,rgba(40,110,200,.55),rgba(40,110,200,0) 70%),radial-gradient(ellipse 300px 120px at 150px 120px,rgba(255,255,255,.7),rgba(255,255,255,0) 70%),radial-gradient(ellipse 320px 110px at 880px 230px,rgba(255,255,255,.8),rgba(255,255,255,0) 70%)}
.brand{font-weight:700;font-size:16px;color:#1e1e1e;letter-spacing:-.2px;white-space:nowrap}
.brand-top{left:112px;top:14px}
.nav{top:18px;font-size:9px;font-weight:700;color:#1e1e1e}
.nav a{position:absolute;white-space:nowrap}
.nav .nav-upload{color:var(--white)}
.search{left:701px;top:11px;width:127px;height:22px;background:var(--white);border:2px solid var(--accent);font-size:7.5px;color:#aaa;padding:5px 0 0 6px}
.search svg{position:absolute;right:6px;top:3px}
.hero-tagline{left:0;width:977px;top:123px;text-align:center;font-size:13px;color:#222}
.btn{display:block;text-align:center;font-weight:700;color:var(--white);font-size:8.5px}
.btn-dark{background:var(--button-dark)}
.btn-accent{background:var(--accent);color:#1e1e1e}
.hero-btn{left:430px;top:154px;width:74px;height:22px;line-height:22px}
.hero-sub{left:0;width:977px;top:184px;text-align:center;font-size:8px;font-weight:700;color:#222}

/* Ad band */
.ad-band{left:0;top:294px;width:977px;height:124px;background:var(--dark-band)}
.ad{top:317px;width:222px;height:74px;background:linear-gradient(120deg,var(--ad-blue) 0%,var(--ad-blue-dark) 55%,#d8dce8 100%);color:var(--white);padding:8px 9px}
.ad-mid{background:linear-gradient(180deg,#6f78a8 0%,#b9a38b 70%,#e7a860 100%)}
.ad-title{font-size:15px;line-height:16px}
.ad-copy{font-size:8px;font-weight:700;line-height:11px;margin-top:4px}
.ad-link{font-size:6.5px;margin-top:4px}

/* Gallery */
.arrow{width:23px;height:20px;background:#e1e1e1;border:1px solid #cfcfcf}
.arrow svg{display:block;margin:4px auto 0}
.thumb{top:458px;width:127px;height:118px}
.t1{left:181px;background:radial-gradient(ellipse 60px 22px at 70px 55px,#e9e9e9,rgba(233,233,233,0) 80%),linear-gradient(180deg,#8e8e8e,#a9a9a9)}
.t2{left:330px;background:radial-gradient(ellipse 55px 45px at 70px 60px,#d6d6d6,rgba(214,214,214,0) 80%),linear-gradient(180deg,#1c1c1c,#4a4a4a 70%,#1e1e1e)}
.t3{left:480px;background:radial-gradient(ellipse 50px 14px at 62px 60px,#dcdcdc,rgba(220,220,220,0) 80%),linear-gradient(180deg,#3e3e3e,#767676)}
.t4{left:628px;background:radial-gradient(ellipse 40px 14px at 50px 40px,#f4f6fa,rgba(244,246,250,0) 80%),linear-gradient(180deg,#8fb6e3,#b8d2ef 75%,#eef2f8)}
.share{left:648px;top:511px;display:flex;gap:5px}
.share a{width:17px;height:17px;background:var(--icon-bg);display:flex;align-items:center;justify-content:center}
.find-more{left:0;width:977px;top:603px;text-align:center;font-size:8px;font-weight:700;color:#555}

/* Discover band */
.sunset{left:0;top:642px;width:977px;height:181px;background:linear-gradient(100deg,var(--sunset-2) 0%,var(--sunset-1) 40%,#d9a07c 65%,var(--sunset-3) 100%)}
.sunset-plane{left:0;top:642px;width:977px;height:181px;background:radial-gradient(ellipse 380px 60px at 640px 148px,rgba(50,50,110,.55),rgba(50,50,110,0) 70%)}
.feature-box{left:323px;top:682px;width:294px;height:105px;background:rgba(255,255,255,.85);text-align:center;padding-top:17px}
.feature-box h2{font-size:12px;font-weight:700;color:#2b2b2b}
.feature-box p{font-size:8px;line-height:12px;color:#333;margin-top:6px}
.feature-btn{width:82px;height:22px;line-height:22px;margin:6px auto 0}

/* Join */
.join-title{left:0;width:977px;top:863px;text-align:center;font-size:13px;color:#333}
.join-copy{left:0;width:977px;top:888px;text-align:center;font-size:7.5px;line-height:9.5px;color:var(--muted)}
.join-btn{left:434px;top:923px;width:70px;height:21px;line-height:21px}

/* Footer */
.footer{left:0;top:980px;width:977px;height:220px;background:linear-gradient(180deg,var(--city-1),var(--city-2))}
.brand-foot{left:0;width:977px;top:1050px;text-align:center;color:var(--white)}
.foot-btn{left:426px;top:1077px;width:86px;height:24px;line-height:24px}
.foot-line{left:0;width:977px;top:1110px;text-align:center;font-size:8px;font-weight:700;color:var(--white)}
.foot-line a{color:var(--accent);text-decoration:underline}
.foot-legal{left:0;width:977px;top:1166px;text-align:center;font-size:7.5px;color:var(--white)}
</style>
</head>
<body>

<div class="abs hero" role="img" aria-label="Photo of a blue and white airliner climbing through a cloudy blue sky"></div>
<div class="abs hero-photo"></div>
<div class="abs brand brand-top">Skyward Lensworks</div>
<nav class="abs nav">
  <a style="left:480px" href="#">Home</a>
  <a style="left:518px" href="#">Gallery</a>
  <a style="left:559px" href="#">Login</a>
  <a style="left:594px" href="#">Register</a>
  <a class="nav-upload" style="left:638px" href="#">Upload Photo</a>
</nav>
<div class="abs search">Enter Search Keywords
  <svg width="13" height="13" viewBox="0 0 13 13"><circle cx="5" cy="5" r="3.5" fill="none" stroke="#f39514" stroke-width="1.8"/><line x1="7.5" y1="7.5" x2="12" y2="12" stroke="#f39514" stroke-width="2.2"/></svg>
</div>
<p class="abs hero-tagline">Lorem Ipsum is simply dummy text of the printing and typesetting industry.</p>
<a class="abs btn btn-dark hero-btn" href="#">Upload Photo</a>
<p class="abs hero-sub">or Discover must see photos</p>

<div class="abs ad-band"></div>
<div class="abs ad" style="left:110px" role="img" aria-label="Advertisement banner with an airliner photo">
  <div class="ad-title">Hotels in Shimla</div>
  <div class="ad-copy">Use Coupon Code "STAY50" &amp; Save Upto 50% On<br>Your Bookings. Hurry!</div>
  <div class="ad-link">tripnest.example/Shimla</div>
</div>
<div class="abs ad ad-mid" style="left:359px" role="img" aria-label="Advertisement banner with a helicopter at sunset">
  <div class="ad-title">Hotels in Shimla</div>
  <div class="ad-copy">Use Coupon Code "STAY50" &amp; Save Upto 50% On<br>Your Bookings. Hurry!</div>
  <div class="ad-link">tripnest.example/Shimla</div>
</div>
<div class="abs ad" style="left:607px" role="img" aria-label="Advertisement banner with an airliner photo">
  <div class="ad-title">Hotels in Shimla</div>
  <div class="ad-copy">Use Coupon Code "STAY50" &amp; Save Upto 50% On<br>Your Bookings. Hurry!</div>
  <div class="ad-link">tripnest.example/Shimla</div>
</div>

<div class="abs arrow" style="left:110px;top:504px"><svg width="8" height="11" viewBox="0 0 8 11"><polyline points="6,1 2,5.5 6,10" fill="none" stroke="#555" stroke-width="1.4"/></svg></div>
<div class="abs arrow" style="left:805px;top:504px"><svg width="8" height="11" viewBox="0 0 8 11"><polyline points="2,1 6,5.5 2,10" fill="none" stroke="#555" stroke-width="1.4"/></svg></div>
<div class="abs thumb t1" role="img" aria-label="Grey-toned photo of a jumbo jet on approach"></div>
<div class="abs thumb t2" role="img" aria-label="Black and white photo of an airliner nose in a hangar"></div>
<div class="abs thumb t3" role="img" aria-label="Monochrome photo of a small propeller plane in flight"></div>
<div class="abs thumb t4" role="img" aria-label="Photo of a jet flying over snowy mountains"></div>
<div class="abs share">
  <a href="#" aria-label="Share photo"><svg width="11" height="11" viewBox="0 0 11 11"><circle cx="8.5" cy="2.2" r="1.6" fill="#fff"/><circle cx="2.3" cy="5.5" r="1.6" fill="#fff"/><circle cx="8.5" cy="8.8" r="1.6" fill="#fff"/><path d="M8.5 2.2L2.3 5.5L8.5 8.8" fill="none" stroke="#fff" stroke-width="1"/></svg></a>
  <a href="#" aria-label="Like photo"><svg width="11" height="11" viewBox="0 0 11 11"><path d="M5.5 9.6L1.5 5.6C.3 4.4.8 2 2.8 1.8c1.2-.1 2 .6 2.7 1.6.7-1 1.5-1.7 2.7-1.6 2 .2 2.5 2.6 1.3 3.8z" fill="#fff"/></svg></a>
  <a href="#" aria-label="Add to favourites"><svg width="11" height="11" viewBox="0 0 11 11"><path d="M5.5 1.5v8M1.5 5.5h8" stroke="#fff" stroke-width="1.8"/></svg></a>
  <a href="#" aria-label="Copy photo link"><svg width="11" height="11" viewBox="0 0 11 11"><rect x="1" y="3.6" width="5.2" height="3.8" rx="1.9" fill="none" stroke="#fff" stroke-width="1.2"/><rect x="4.8" y="3.6" width="5.2" height="3.8" rx="1.9" fill="none" stroke="#fff" stroke-width="1.2"/></svg></a>
</div>
<p class="abs find-more">Find More</p>

<div class="abs sunset" role="img" aria-label="Photo of a jet banking against an orange sunset sky"></div>
<div class="abs sunset-plane"></div>
<div class="abs feature-box">
  <h2>Lorem Ipsum</h2>
  <p>Lorem Ipsum is simply dummy text of the printing and typesetting industry.<br>Lorem Ipsum has been</p>
  <a class="btn btn-dark feature-btn" href="#">Discover Photos</a>
</div>

<p class="abs join-title">Lorem Ipsum is simply dummy text</p>
<p class="abs join-copy">Lorem Ipsum is simply dummy text of the printing and<br>typesetting industry. Lorem Ipsum has been</p>
<a class="abs btn btn-accent join-btn" href="#">Join US</a>

<div class="abs footer" role="img" aria-label="Darkened aerial photo of a city skyline"></div>
<div class="abs brand brand-foot">Skyward Lensworks</div>
<a class="abs btn btn-accent foot-btn" href="#">Create Account</a>
<p class="abs foot-line">Lorem Ipsum dummy text &nbsp;|&nbsp; <a href="#">Lorem Ipsum</a></p>
<p class="abs foot-legal">About Us &nbsp;|&nbsp; Privacy Policy &nbsp;|&nbsp; 2014 Copyright Company Name</p>

</body>
</html>
```